New business card design needed for Diesel Fitting (Mechanical) Company

We need a new business card for our company called "Gumtree Engine Works" that showcases our logo and business details.
Target Market(s)
Owners of all makes and models of vehicles, trucks, plant and machinery.
Industry/Entity Type
Mechanical
Contact Information for Business Card
The business card details need to include the following: Owners/Directors: Doug & Marisol Brent-Coyle ABN: 41 917 302 846 Address: 317 Wattlebrook Street CHARTERS TOWERS QLD 4820 Postal Address: PO Box 5791 CHARTERS TOWERS QLD 4820 Website: www.gewservice.com.au Phone: 4712 9083 Mobile: 0438 175 906 Emails: sales@gewservice.com.au; admin@gewservice.com.au; accounts@gewservice.com.au; parts@gewservice.com.au; office@gewservice.com.au, reception@gewservice.com.au
Look and feel

```html
<!DOCTYPE html>
<html lang="en">
<head>
<meta charset="utf-8">
<title>Gumtree Engine Works – Business Card</title>
<link rel="stylesheet" href="https://fonts.googleapis.com/css2?family=Arimo:wght@400;700&family=Questrial&display=swap">
<style>
  :root {
    --stage: #3a3a3a;
    --paper: #ffffff;
    --red: #e8202a;
    --yellow: #fcc21b;
    --yellow-dark: #e0a30f;
    --orange: #f26f21;
    --ink: #222222;
    --black: #050505;
    --charcoal: #2a2a2a;
    --white: #ffffff;
  }
  * { box-sizing: border-box; margin: 0; padding: 0; }
  html, body { width: 1200px; height: 900px; overflow: hidden; }
  body {
    background: var(--stage);
    font-family: "Arimo", Arial, sans-serif;
    position: relative;
  }
  .card {
    position: absolute;
    left: 270px;
    width: 660px;
    height: 377px;
    overflow: hidden;
    box-shadow: 0 10px 24px rgba(0,0,0,.45);
  }
  /* ---------- Front ---------- */
  .card-front { top: 53px; background: var(--paper); }
  .front-brand {
    position: absolute; left: 0; top: 0; width: 300px; height: 100%;
    display: flex; align-items: center; justify-content: center; gap: 12px;
  }
  .brand-dot {
    width: 26px; height: 26px; border-radius: 50%;
    background: var(--orange); flex: none;
  }
  .front-brand .brand-name {
    font-family: "Questrial", sans-serif;
    font-size: 25px; line-height: 1.1; color: var(--ink);
  }
  .front-panel {
    position: absolute; left: 300px; top: 0; right: 0; bottom: 0;
    background: var(--red);
    color: var(--white);
    text-align: right;
    padding: 16px 22px 0 0;
  }
  .owners {
    font-weight: 700; font-size: 21px; color: var(--yellow); line-height: 1.1;
  }
  .role { font-size: 12px; line-height: 1.2; }
  .abn { font-size: 10px; }
  .abn b { margin-right: 4px; }
  .contact-row {
    display: flex; justify-content: flex-end; align-items: flex-start; gap: 10px;
  }
  .icon { width: 13px; height: 13px; flex: none; fill: var(--yellow); }
  .address { margin-top: 22px; font-size: 13px; line-height: 1.35; }
  .phones { margin-top: 18px; font-size: 13px; line-height: 1.35; }
  .icon-stack { display: flex; flex-direction: column; gap: 5px; padding-top: 2px; }
  .emails { margin-top: 4px; margin-right: 23px; font-size: 12.5px; line-height: 1.3; }
  .postal-band {
    position: absolute; left: 270px; right: 0; bottom: 14px; height: 26px;
    background: var(--yellow);
    color: var(--white);
    font-size: 12px; line-height: 26px;
    padding-left: 50px;
  }
  .postal-band b { font-weight: 700; }
  .postal-band::before {
    content: ""; position: absolute; left: 0; top: -8px;
    border-right: 14px solid var(--yellow-dark);
    border-top: 8px solid transparent;
  }
  /* ---------- Back ---------- */
  .card-back {
    top: 470px;
    background: linear-gradient(90deg, var(--black) 0 52%, var(--charcoal) 52% 100%);
  }
  .back-brand {
    position: absolute; left: 0; right: 0; top: 110px;
    display: flex; align-items: center; justify-content: center; gap: 16px;
  }
  .back-brand .brand-dot { width: 34px; height: 34px; }
  .back-brand .brand-name {
    font-family: "Questrial", sans-serif;
    font-size: 38px; color: var(--orange); line-height: 1;
  }
  .website {
    position: absolute; left: 0; right: 0; bottom: 52px;
    text-align: center; color: var(--white);
    font-size: 15px; letter-spacing: 2.5px;
  }
  .services-band {
    position: absolute; left: 0; right: 0; bottom: 12px; height: 28px;
    background: var(--orange);
    display: flex; justify-content: center; align-items: center;
    color: var(--white); font-size: 13px; letter-spacing: .3px;
  }
  .services-band span + span { border-left: 1px solid var(--white); margin-left: 8px; padding-left: 8px; }
</style>
</head>
<body>

<section class="card card-front">
  <div class="front-brand">
    <span class="brand-dot"></span>
    <span class="brand-name">Gumtree Engine Works</span>
  </div>
  <div class="front-panel">
    <p class="owners">Doug &amp; Marisol Brent-Coyle</p>
    <p class="role">Owners/Directors</p>
    <p class="abn"><b>ABN</b>41 917 302 846</p>

    <div class="contact-row address">
      <p>317 Wattlebrook Street<br>CHARTERS TOWERS QLD 4820</p>
      <svg class="icon" viewBox="0 0 16 16"><path d="M8 1a5 5 0 0 0-5 5c0 3.6 5 9 5 9s5-5.4 5-9a5 5 0 0 0-5-5zm0 7a2 2 0 1 1 0-4 2 2 0 0 1 0 4z"/></svg>
    </div>

    <div class="contact-row phones">
      <p>4712 9083<br>0438 175 906</p>
      <div class="icon-stack">
        <svg class="icon" viewBox="0 0 16 16"><path d="M3.5 1l2.5 3-1.5 2a8 8 0 0 0 5 5l2-1.5 3 2.5-1.5 2.5C7 15 1 9 1 2.5z"/></svg>
        <svg class="icon" viewBox="0 0 16 16"><path d="M4.5 1h7v14h-7zM6 2.5v9h4v-9zm2 10a.8.8 0 1 0 0 1.6.8.8 0 0 0 0-1.6z" fill-rule="evenodd"/></svg>
        <svg class="icon" viewBox="0 0 16 16"><path d="M1 3h14v10H1zm1.5 1.5L8 9l5.5-4.5z" fill-rule="evenodd"/></svg>
      </div>
    </div>

    <p class="emails">
      sales@gewservice.com.au<br>
      admin@gewservice.com.au<br>
      accounts@gewservice.com.au<br>
      parts@gewservice.com.au<br>
      office@gewservice.com.au<br>
      reception@gewservice.com.au
    </p>
  </div>
  <div class="postal-band"><b>PO Box</b> 5791 CHARTERS TOWERS QLD 4820</div>
</section>

<section class="card card-back">
  <div class="back-brand">
    <span class="brand-dot"></span>
    <span class="brand-name">Gumtree Engine Works</span>
  </div>
  <p class="website">www.gewservice.com.au</p>
  <div class="services-band">
    <span>FULL MECHANICAL</span>
    <span>FIELD SERVICE</span>
    <span>AIR CONDITIONING</span>
    <span>AUTO ELECTRICAL</span>
    <span>HYDRAULIC</span>
  </div>
</section>

</body>
</html>
```